electrical contractor business card for professional modern company

I need a business card design for an electrical contractors business. I do all kinds of electricical work from new homes, air conditioning, data and communications. I have a logo design i want on it and have a good idea in my head of what i want it to look like. I like simple yet bold and professional looking. All black background is a must

Target Market(s)

Anyone needing electrical work done

Industry/Entity Type

Electrical

Contact Information for Business Card

company name- KMP Electrical and Data
person name-lewis pembury
phone number- 0468 239 517
website-kmpwire-sample.com.au

Font styles to use
Sans Serif

Requirements
Must have
• email
• website
• logo
• name
• phone number
• list of work i do:
• -electrical
• -air-conditioning
• -data/communications
• -cctv/security
• -domestic/commercial/industrial
• -24hr emergency breakdown repair
Nice to have
• i would like the logo on the front side in the centre taking up most of the card with black background.
• on the rear i want the list of work i do with company info i.e. email, website, my name, phone number. rear of card also black background with orange writing to match the orange in the logo

```html
<!DOCTYPE html>
<html lang="en">
<head>
<meta charset="utf-8">
<title>KMP Electrical and Data – Business Card</title>
<link rel="stylesheet" href="https://fonts.googleapis.com/css2?family=Montserrat:wght@400;600;700;800&display=swap">
<style>
  :root {
    --backdrop: #e9e6e1;
    --card-black: #1f1f1f;
    --card-white: #f4f4f4;
    --card-grey: #dcdcdc;
    --orange: #f26a1b;
    --white: #ffffff;
    --ink: #2a2a2a;
    --muted: #cfcfcf;
  }
  * { box-sizing: border-box; margin: 0; padding: 0; }
  html, body {
    width: 1200px; height: 828px; overflow: hidden;
    background: var(--backdrop);
    font-family: "Montserrat", Arial, sans-serif;
  }
  .canvas {
    position: relative; width: 1200px; height: 828px;
    display: flex; align-items: center; justify-content: center; gap: 44px;
  }
  .card {
    position: relative; width: 540px; height: 310px;
    border-radius: 4px; overflow: hidden;
    box-shadow: 0 10px 28px rgba(0,0,0,0.18);
  }

  /* Front */
  .card--front { background: var(--card-black); }
  .front-mark {
    position: absolute; inset: 0;
    display: flex; flex-direction: column; align-items: center; justify-content: center;
    color: var(--white);
  }
  .front-mark__row { display: flex; align-items: center; gap: 16px; }
  .front-mark__dot { width: 26px; height: 26px; border-radius: 50%; background: var(--orange); }
  .front-mark__name { font-weight: 700; font-size: 96px; letter-spacing: 4px; line-height: 1; }
  .front-mark__tag {
    margin-top: 8px; font-weight: 700; font-size: 17px; letter-spacing: 3.5px;
    text-transform: uppercase;
  }

  /* Back */
  .card--back { background: linear-gradient(180deg, var(--card-white) 0%, var(--card-grey) 60%); }
  .back-shape { position: absolute; inset: 0; width: 100%; height: 100%; }
  .back-mark { position: absolute; left: 150px; top: 58px; color: var(--ink); }
  .back-mark__row { display: flex; align-items: center; gap: 8px; }
  .back-mark__dot { width: 12px; height: 12px; border-radius: 50%; background: var(--orange); }
  .back-mark__name { font-weight: 700; font-size: 46px; letter-spacing: 2px; line-height: 1; }
  .back-mark__tag {
    margin-top: 4px; font-weight: 700; font-size: 9px; letter-spacing: 1.8px; text-transform: uppercase;
  }

  .holder {
    position: absolute; left: 40px; bottom: 52px; color: var(--white);
    text-transform: uppercase;
  }
  .holder__name { font-weight: 600; font-size: 13px; letter-spacing: 0.6px; }
  .holder__role { font-weight: 400; font-size: 10px; letter-spacing: 0.6px; color: var(--muted); margin-top: 2px; }

  .contact {
    position: absolute; left: 262px; top: 186px; width: 256px;
    color: var(--white); font-size: 8px; line-height: 1.5;
  }
  .contact__address { margin-bottom: 8px; }
  .contact__grid { display: grid; grid-template-columns: auto 1fr; column-gap: 14px; row-gap: 4px; }
  .contact__item { display: flex; align-items: center; gap: 5px; white-space: nowrap; }
  .contact__icon { width: 9px; height: 9px; flex: none; fill: var(--white); }

  .services {
    position: absolute; left: 262px; top: 262px; width: 256px;
    color: var(--orange); font-size: 7px; font-weight: 600; line-height: 1.5;
    letter-spacing: 0.3px; text-transform: uppercase;
  }
</style>
</head>
<body>
<main class="canvas">

  <section class="card card--front" aria-label="Card front">
    <div class="front-mark">
      <div class="front-mark__row">
        <span class="front-mark__dot"></span>
        <span class="front-mark__name">KMP</span>
      </div>
      <div class="front-mark__tag">Electrical and Data</div>
    </div>
  </section>

  <section class="card card--back" aria-label="Card back">
    <svg class="back-shape" viewBox="0 0 540 310" preserveAspectRatio="none" aria-hidden="true">
      <path d="M0 218 C 150 200, 330 150, 540 70 L540 310 L0 310 Z" fill="var(--orange)"/>
      <path d="M0 230 C 150 212, 330 162, 540 82 L540 310 L0 310 Z" fill="var(--card-black)"/>
    </svg>

    <div class="back-mark">
      <div class="back-mark__row">
        <span class="back-mark__dot"></span>
        <span class="back-mark__name">KMP</span>
      </div>
      <div class="back-mark__tag">Electrical and Data</div>
    </div>

    <div class="contact">
      <div class="contact__address">27 Volt Street<br>Landline Road</div>
      <div class="contact__grid">
        <div class="contact__item">
          <svg class="contact__icon" viewBox="0 0 10 10"><path d="M2 0.5 L3.8 2.6 L2.9 3.6 Q4 5.8 6.4 7.1 L7.4 6.2 L9.5 8 L8.3 9.5 Q3.5 8.8 0.5 1.8 Z"/></svg>
          <span>0468 239 517</span>
        </div>
        <div class="contact__item">
          <svg class="contact__icon" viewBox="0 0 10 10"><path d="M0.5 2 H9.5 V8 H0.5 Z M1 2.5 L5 5.4 L9 2.5" fill="none" stroke="#fff" stroke-width="1"/></svg>
          <span>info@kmpwire-sample.com.au</span>
        </div>
        <div class="contact__item">
          <svg class="contact__icon" viewBox="0 0 10 10"><rect x="1" y="3" width="8" height="5" rx="1"/><rect x="3" y="1" width="4" height="2.5"/></svg>
          <span>0468 239 518</span>
        </div>
        <div class="contact__item">
          <svg class="contact__icon" viewBox="0 0 10 10"><circle cx="5" cy="5" r="4.2" fill="none" stroke="#fff" stroke-width="1"/><path d="M0.8 5 H9.2 M5 0.8 Q2.6 5 5 9.2 M5 0.8 Q7.4 5 5 9.2" fill="none" stroke="#fff" stroke-width="0.8"/></svg>
          <span>www.kmpwire-sample.com.au</span>
        </div>
      </div>
    </div>

    <ul class="services" aria-label="Services">
      <li>Electrical · Air-conditioning · Data/Communications · CCTV/Security</li>
      <li>Domestic/Commercial/Industrial · 24hr Emergency Breakdown Repair</li>
    </ul>

    <div class="holder">
      <div class="holder__name">Lewis Pembury</div>
      <div class="holder__role">President</div>
    </div>
  </section>

</main>
<style>.services { list-style: none; }</style>
</body>
</html>
```